Podcast Cover Design - Headline At Quiet Tables

We renamed our podcast from the "Harborline Property Podcast" to "Headlines At Quiet Tables" and we need a new podcast cover design, Instagram profile picture, and a YouTube banner.

More so we're looking for some sort of symbol/icon. Our old logo had the Copper Lantern but we're moving to a much broader audience that isn't necessarily from Seattle and needs something that will appeal to them.

In the podcast, Dale reads the news that big media isn't covering including crime, business, homeless crisis, protests. We stay away from covering politics but our audience is mainly right-wing.

Attached are some additional designs we created in-house.

If we love the design we'll have additional job opportunities to create possible designs for merchandise.

Target Market(s)

80% Males aged 50+, Republican

Industry/Entity Type

News

Colors

Designer to choose colors to be used in the design.

Requirements
Must have
• OPEN TOO IDEAS
Nice to have
• OPEN TOO IDEAS
Should not have
• Copper Lantern

```html
<!DOCTYPE html>
<html lang="en">
<head>
<meta charset="utf-8">
<title>Headlines At Quiet Tables – Podcast Cover</title>
<link rel="stylesheet" href="https://fonts.googleapis.com/css2?family=Bebas+Neue&family=Outfit:wght@400;600;700;800&display=swap">
<style>
  :root {
    --cover-red: #cb1c1e;
    --band-dark: #1d1c1c;
    --ink-white: #ffffff;
    --ink-dark: #1a1a1a;
    --portrait-light: #bdbdbd;
    --portrait-dark: #3a3a3a;
  }
  html, body {
    margin: 0;
    padding: 0;
    width: 1200px;
    height: 1200px;
    overflow: hidden;
    background: var(--cover-red);
  }
  .cover {
    display: block;
    width: 1200px;
    height: 1200px;
  }
  .title-main {
    font-family: "Outfit", sans-serif;
    font-weight: 800;
    fill: var(--ink-white);
  }
  .title-tag {
    font-family: "Outfit", sans-serif;
    font-weight: 800;
    fill: var(--ink-white);
  }
  .title-band {
    font-family: "Bebas Neue", "Outfit", sans-serif;
    fill: var(--ink-white);
  }
  .byline-by {
    font-family: "Outfit", sans-serif;
    font-weight: 400;
    fill: var(--ink-white);
  }
  .byline-name {
    font-family: "Outfit", sans-serif;
    font-weight: 700;
    fill: var(--ink-white);
  }
  .format-label {
    font-family: "Outfit", sans-serif;
    font-weight: 600;
    fill: var(--ink-dark);
    letter-spacing: 7px;
  }
</style>
</head>
<body>
<svg class="cover" viewBox="0 0 1200 1200" xmlns="http://www.w3.org/2000/svg">
  <defs>
    <linearGradient id="portraitTone" x1="0" y1="0" x2="0" y2="1">
      <stop offset="0" stop-color="var(--portrait-dark)"/>
      <stop offset="0.35" stop-color="var(--portrait-light)"/>
      <stop offset="1" stop-color="#6e6e6e"/>
    </linearGradient>
    <linearGradient id="bandTone" x1="0" y1="0" x2="1" y2="1">
      <stop offset="0" stop-color="#2a2929"/>
      <stop offset="1" stop-color="#151414"/>
    </linearGradient>
  </defs>

  <rect class="background" width="1200" height="1200" fill="var(--cover-red)"/>

  <!-- Title: first line -->
  <text class="title-main" x="95" y="381" font-size="178" textLength="1011" lengthAdjust="spacingAndGlyphs">HEADLINES</text>

  <!-- Title: second line with boxed tag word -->
  <rect class="tag-box" x="95" y="424" width="48" height="97" fill="var(--ink-dark)"/>
  <text class="title-tag" transform="translate(130 472) rotate(-90)" text-anchor="middle" font-size="34">AT</text>
  <text class="title-main" x="153" y="521" font-size="136">QUIET</text>

  <!-- Dark band with last title word -->
  <rect class="title-band-bg" x="453" y="604" width="747" height="299" fill="url(#bandTone)" role="img" aria-label="Dark brick wall texture behind the title word"/>
  <text class="title-band" x="548" y="843" font-size="250" textLength="562" lengthAdjust="spacingAndGlyphs">TABLES</text>

  <!-- Host portrait area -->
  <path class="portrait-outline" d="M-10 1200 V1030 Q50 985 110 975 L108 700 Q120 540 330 528 Q535 540 548 716 L540 975 Q640 1000 760 1200 Z" fill="none" stroke="var(--ink-white)" stroke-opacity="0.6" stroke-width="2"/>
  <path class="host-portrait" d="M0 1200 V1040 Q60 992 122 982 L120 704 Q132 556 330 545 Q522 556 532 718 L524 982 Q606 1004 710 1200 Z" fill="url(#portraitTone)" stroke="var(--ink-white)" stroke-width="2" role="img" aria-label="Black and white portrait of the host, Dale Whitcombe"/>

  <!-- Byline -->
  <text x="552" y="1013">
    <tspan class="byline-by" font-size="48">by </tspan><tspan class="byline-name" font-size="56">DALE WHITCOMBE</tspan>
  </text>

  <!-- Format label -->
  <text class="format-label" x="1112" y="1112" text-anchor="end" font-size="29">PODCAST</text>
</svg>
</body>
</html>
```